Marlo Tidy Yard Website

We need a website design for this new company. I've attached the company logo. This company is in the construction industry that provides general labor, maintenance and cleaning for construction sites. We want a clean and simple website that can be easy to navigate.

Target Market(s)

Construction industry

Industry/Entity Type

Construction

Number of Pages Required

2 page

Font styles to use
Sans Serif

```html
<!DOCTYPE html>
<html lang="en">
<head>
<meta charset="utf-8">
<title>Marlo Tidy Yard</title>
<link href="https://fonts.googleapis.com/css2?family=Raleway:wght@600;700;800&family=Open+Sans:ital,wght@0,400;0,600;0,700;1,400&display=swap" rel="stylesheet">
<style>
:root{
  --navy:#14146e;
  --orange:#f26b12;
  --orange-soft:#f7a35a;
  --ink:#222;
  --muted:#6b6b6b;
  --dark:#17181b;
  --card:#f1f1f1;
  --white:#fff;
  --footer:#232427;
  --bottom:#0e0e6c;
}
*{margin:0;padding:0;box-sizing:border-box}
html,body{width:1200px;height:3475px;overflow:hidden;background:var(--white)}
body{position:relative;font-family:"Open Sans",Arial,sans-serif;color:var(--ink)}
.abs{position:absolute}
.heading{font-family:"Raleway",Arial,sans-serif;font-weight:800;color:var(--navy);text-align:center;font-size:38px;letter-spacing:.5px}
.rule{position:absolute;left:574px;width:52px;height:4px;background:var(--orange)}

/* header */
.site-header{left:0;top:0;width:1200px;height:93px;background:var(--white)}
.brand{left:81px;top:22px;display:flex;align-items:center;gap:10px;font-family:"Raleway",sans-serif;font-weight:800;font-size:22px;color:var(--navy);line-height:1}
.brand-mark{width:18px;height:18px;background:var(--orange)}
.nav{left:396px;top:38px;display:flex;gap:0;font-size:14px;color:#444;letter-spacing:.3px}
.nav span{position:absolute;white-space:nowrap}
.nav .active{color:var(--navy)}
.nav .active::before{content:"";position:absolute;left:0;top:-8px;width:22px;height:3px;background:var(--orange)}
.nav-divider{left:931px;top:36px;width:1px;height:26px;background:#ccc}
.phone{left:971px;top:38px;font-size:14px;color:#444}

/* hero */
.hero{left:0;top:93px;width:1200px;height:521px;background:linear-gradient(90deg,#f5721c 0%,#f48a3c 45%,#c7b58d 75%,#9a8a6e 100%)}
.hero-title{left:81px;top:270px;font-family:"Raleway",sans-serif;font-weight:700;font-size:40px;line-height:50px;color:var(--white)}
.hero-sub{left:81px;top:386px;width:380px;font-size:17px;font-weight:600;line-height:27px;color:var(--white)}

/* welcome */
.welcome-title{left:0;top:662px;width:1200px}
.lead{left:266px;top:745px;width:668px;font-style:italic;font-size:17px;line-height:29px;color:var(--muted);text-align:center}
.body-copy{left:258px;top:848px;width:684px;font-size:13px;line-height:25px;color:var(--muted);text-align:center}

/* services */
.services-band{left:0;top:991px;width:1200px;height:406px;background:linear-gradient(180deg,#1d1e22,#121316)}
.ghost{left:0;top:1058px;width:1200px;text-align:center;font-family:"Raleway",sans-serif;font-weight:800;font-size:48px;color:rgba(255,255,255,.08);letter-spacing:2px}
.services-title{left:0;top:1060px;width:1200px;color:var(--orange)}
.services-rule{top:1118px;background:var(--white)}
.service{width:322px;height:396px;top:1179px}
.service-photo{width:322px;height:218px}
.service-body{height:178px;background:var(--card);text-align:center;padding:30px 28px 0}
.service.featured .service-body{background:var(--white);box-shadow:0 6px 18px rgba(0,0,0,.12)}
.service h3{font-family:"Raleway",sans-serif;font-weight:700;font-size:21px;color:var(--ink);margin-bottom:14px}
.service p{font-size:13px;line-height:25px;color:var(--muted)}

/* testimonials */
.testimonials-title{left:0;top:1653px;width:1200px}
.testimonial-photo{left:185px;top:1749px;width:686px;height:375px;background:linear-gradient(120deg,#6f6f6a,#b9b7a8 45%,#8c8e8a)}
.quote-card{left:419px;top:2062px;width:600px;height:185px;background:var(--white);box-shadow:0 6px 22px rgba(0,0,0,.14);padding:32px 40px}
.quote-card p{font-size:13px;line-height:25px;color:var(--muted)}
.quote-card .client{margin-top:14px;font-size:14px;color:var(--ink)}
.arrow{width:40px;height:40px;border:1px solid #ccc;background:var(--white);display:flex;align-items:center;justify-content:center}

/* cta */
.cta{left:0;top:2340px;width:1200px;height:234px;background:linear-gradient(90deg,#1d1f7a,#2b2d96 55%,#1a1b6e)}
.cta-text{left:81px;top:2412px;width:660px;font-family:"Raleway",sans-serif;font-weight:700;font-size:34px;line-height:46px;color:var(--orange)}
.cta-btn{left:883px;top:2435px;width:238px;height:53px;border-radius:27px;background:var(--orange);color:var(--navy);font-family:"Raleway",sans-serif;font-weight:800;font-size:17px;display:flex;align-items:center;justify-content:center}

/* news */
.news-title{left:0;top:2624px;width:1200px}
.news-photo{width:272px;height:271px;top:2715px}
.news-card{width:268px;height:122px;top:2924px;background:var(--white);box-shadow:0 6px 18px rgba(0,0,0,.12);padding:22px 20px}
.news-card p{font-size:15px;line-height:27px;color:var(--ink)}
.news-card.featured p{color:var(--orange)}
.news-card .date{font-size:13px;color:var(--muted);margin-top:6px}

/* footer */
.site-footer{left:0;top:3132px;width:1200px;height:278px;background:var(--footer)}
.footer-brand{left:81px;top:3190px;display:flex;align-items:center;gap:10px;font-family:"Raleway",sans-serif;font-weight:800;font-size:22px;color:var(--white)}
.footer-about{left:81px;top:3260px;width:300px;font-size:13px;line-height:27px;color:#ddd}
.footer-head{font-family:"Raleway",sans-serif;font-weight:700;font-size:19px;color:var(--white)}
.links{font-size:13px;color:#ddd;line-height:37px}
.links li{list-style:none;padding-left:24px;position:relative}
.links li::before{content:"";position:absolute;left:0;top:16px;width:12px;height:3px;background:var(--orange)}
.contact-row{display:flex;gap:16px;font-size:13px;line-height:24px;color:#ddd}
.contact-row svg{flex:none;margin-top:3px}
.bottom-bar{left:0;top:3410px;width:1200px;height:65px;background:var(--bottom);color:#e6e6f5;font-size:13px;display:flex;align-items:center;justify-content:center}
</style>
</head>
<body>

<header class="abs site-header">
  <div class="abs brand"><span class="brand-mark"></span>MARLO TIDY YARD</div>
  <nav class="abs nav">
    <span class="active" style="left:0">HOME</span>
    <span style="left:67px">ABOUT</span>
    <span style="left:144px">SERVICES</span>
    <span style="left:236px">TESTIMONIALS</span>
    <span style="left:359px">NEWS</span>
    <span style="left:426px">CONTACT</span>
  </nav>
  <div class="abs nav-divider"></div>
  <div class="abs phone">PHONE : 123 456 7890</div>
</header>

<section class="abs hero" role="img" aria-label="Photo of construction workers in hard hats and safety vests reviewing plans, under an orange overlay"></section>
<h1 class="abs hero-title">LOREM IPSUM IS<br>SIMPLY DUMMY.</h1>
<p class="abs hero-sub">Lorem Ipsum is simply dummy text of the printing and typesetting industry.</p>

<h2 class="abs heading welcome-title">WELCOME TO MARLO TIDY YARD</h2>
<div class="rule" style="top:721px"></div>
<p class="abs lead">Lorem Ipsum is simply dummy text of the printing and typesetting industry. Lorem Ipsum has been the industry's standard dummy text ever since the 1500s, when an unknown printer took a galley of type and scrambled it to make a type.</p>
<p class="abs body-copy">Lorem Ipsum is simply dummy text of the printing and typesetting industry. Lorem Ipsum has been the industry's standard dummy text ever since the 1500s, when an unknown printer took a galley of type and scrambled it to make a type specimen book. It has survived not only five centuries.</p>

<section class="abs services-band" role="img" aria-label="Dark photo of a construction site behind the services heading"></section>
<div class="abs ghost">SERVICES WE PROVIDE</div>
<h2 class="abs heading services-title">SERVICES WE PROVIDE</h2>
<div class="rule services-rule"></div>

<article class="abs service" style="left:76px">
  <div class="service-photo" role="img" aria-label="Photo of a labourer in a yellow hard hat carrying timber" style="background:linear-gradient(135deg,#c8702a,#8a4b1c)"></div>
  <div class="service-body"><h3>General labor</h3><p>Lorem Ipsum is simply dummy text of the printing and typesetting industry. Lorem Ipsum has been the industry's standard dummy.</p></div>
</article>
<article class="abs service featured" style="left:438px">
  <div class="service-photo" role="img" aria-label="Photo of two workers in safety vests inspecting a steel structure" style="background:linear-gradient(135deg,#b7a996,#6d5e4f)"></div>
  <div class="service-body"><h3>Maintenance</h3><p>Lorem Ipsum is simply dummy text of the printing and typesetting industry. Lorem Ipsum has been the industry's standard dummy.</p></div>
</article>
<article class="abs service" style="left:799px">
  <div class="service-photo" role="img" aria-label="Photo of a worker vacuuming a floor with an industrial cleaner" style="background:linear-gradient(135deg,#d9d6d1,#8c8a86)"></div>
  <div class="service-body"><h3>Cleaning</h3><p>Lorem Ipsum is simply dummy text of the printing and typesetting industry. Lorem Ipsum has been the industry's standard dummy.</p></div>
</article>

<h2 class="abs heading testimonials-title">TESTIMONIALS</h2>
<div class="rule" style="top:1712px"></div>
<div class="abs testimonial-photo" role="img" aria-label="Photo of a smiling worker in a hard hat and vest holding a coffee cup in a warehouse"></div>
<div class="abs quote-card">
  <p>Lorem Ipsum is simply dummy text of the printing and typesetting industry. Lorem Ipsum has been the industry's standard dummy text ever since the 1500s, when an unknown printer took a galley of type.</p>
  <p class="client">- CLIENT NAME</p>
</div>
<div class="abs arrow" style="left:185px;top:2145px"><svg width="12" height="16" viewBox="0 0 12 16"><path d="M9 2 3 8l6 6" fill="none" stroke="#f26b12" stroke-width="2.5"/></svg></div>
<div class="abs arrow" style="left:239px;top:2145px"><svg width="12" height="16" viewBox="0 0 12 16"><path d="m3 2 6 6-6 6" fill="none" stroke="#f26b12" stroke-width="2.5"/></svg></div>

<section class="abs cta" role="img" aria-label="Photo of workers on site under a deep blue overlay"></section>
<p class="abs cta-text">Lorem Ipsum is simply dummy text of the printing and typesetting industry.</p>
<div class="abs cta-btn">CONTACT US NOW</div>

<h2 class="abs heading news-title">LATEST NEWS</h2>
<div class="rule" style="top:2683px"></div>

<div class="abs news-photo" style="left:76px;background:linear-gradient(135deg,#e3b24c,#9b6d3a)" role="img" aria-label="Photo of a young worker in a yellow hard hat"></div>
<div class="abs news-card" style="left:130px"><p>Lorem Ipsum is simply dummy text of the printing.</p><p class="date">6 JAN 2019</p></div>

<div class="abs news-photo" style="left:438px;background:linear-gradient(135deg,#f07a26,#e0631a)" role="img" aria-label="Photo of a construction site under an orange hover overlay"></div>
<svg class="abs" style="left:561px;top:2838px" width="26" height="26" viewBox="0 0 26 26" aria-hidden="true"><g fill="none" stroke="#14146e" stroke-width="3" stroke-linecap="round"><path d="M11 15 15 11"/><path d="M13 7l2-2a4.2 4.2 0 0 1 6 6l-2 2"/><path d="M13 19l-2 2a4.2 4.2 0 0 1-6-6l2-2"/></g></svg>
<div class="abs news-card featured" style="left:492px"><p>Lorem Ipsum is simply dummy text of the printing.</p><p class="date">6 JAN 2019</p></div>

<div class="abs news-photo" style="left:799px;background:linear-gradient(135deg,#5d5a55,#2f2d2a)" role="img" aria-label="Photo of a worker tying steel reinforcement bars"></div>
<div class="abs news-card" style="left:853px"><p>Lorem Ipsum is simply dummy text of the printing.</p><p class="date">6 JAN 2019</p></div>

<footer class="abs site-footer">
</footer>
<div class="abs footer-brand"><span class="brand-mark"></span>MARLO TIDY YARD</div>
<p class="abs footer-about">Lorem Ipsum is simply dummy text of the printing and typesetting industry. Lorem Ipsum has been the industry's standard dummy text.</p>

<h4 class="abs footer-head" style="left:441px;top:3180px">SITE MAP</h4>
<ul class="abs links" style="left:441px;top:3213px"><li>Home</li><li>About us</li><li>Services</li><li>Testimonials</li></ul>
<ul class="abs links" style="left:625px;top:3213px"><li>News</li><li>Contact</li><li>Privacy Policy</li></ul>

<h4 class="abs footer-head" style="left:801px;top:3180px">CONTACT INFO</h4>
<div class="abs contact-row" style="left:799px;top:3218px;width:290px">
  <svg width="16" height="20" viewBox="0 0 16 20"><path d="M8 0a7 7 0 0 1 7 7c0 5-7 13-7 13S1 12 1 7a7 7 0 0 1 7-7z" fill="#f26b12"/><circle cx="8" cy="7" r="2.6" fill="#232427"/></svg>
  <span>Lorem Ipsum is simply dummy text of the printing and typesetting industry.</span>
</div>
<div class="abs contact-row" style="left:799px;top:3283px">
  <svg width="16" height="18" viewBox="0 0 16 18"><path d="M3 1l3 0 2 4-2 2a10 10 0 0 0 4 4l2-2 4 2v3c0 1-1 2-2 2C7 16 1 10 1 3c0-1 1-2 2-2z" fill="#f26b12"/></svg>
  <span>123 456 7890</span>
</div>
<div class="abs contact-row" style="left:799px;top:3321px">
  <svg width="18" height="14" viewBox="0 0 18 14"><rect x="0" y="1" width="18" height="12" rx="1.5" fill="#f26b12"/><path d="M1 2l8 6 8-6" fill="none" stroke="#232427" stroke-width="1.5"/></svg>
  <span>info@marlotidyyard.com</span>
</div>

<div class="abs bottom-bar">©MARLO TIDY YARD. 2018 - All Rights Reserved.</div>

</body>
</html>
```